Ortel Ridge Wine Club-The Velvet Roll

We are a new aspirational brand of fine Tasmania Wine. We need a commitment club poster which appeals to the ego.We have one opportunity to get customers to sign up and that is when they visit at the cellar door. This club is the core of our business.

The brand is a clean, pure , simple brand, black and white very sophiscated.
This is a top end product.

Our Commitment Club is named The Velvet Roll which is a play on words. Tradionally the velvet roll is a list of people that you dont want to do business with. So we are turning this on its had.

You need to make this poster sharp, desirable, possibly sexy but masculine. Im thinking Conrad Vale . It doesnt matter the client will be 40 up fashion consious looking for something new , exclusive , something there peers don't have.

I dont like busy! make it clean clear and basically undeniable. The client must not be able to resist the offer.

www.ortelridge-example.com.au

Target Market(s)

Appreciator 40-60 male wants to be recognised fashion consious sophiscated has money and wants to part of something exclusive.

A feeling that you are part of something that only a few are. Exclusive

Maybe an imagine of beautiful people 30/40ish I want to be drinking Ortel Wine / in the velvet roll

Industry/Entity Type

Fashion

Requirements
Must have
• Ortel Ridge Logo
ORTEL Bottles images

We produce only 1600 cases of wine each vintage. Therefore we have limited membership 001-999 for our club.
Award Winning Wines available exclusively from us.

Gold Member
We will reserve 2 cases of our limited vintage, to be delivered to you in May and Oct.
Single varietal or mixed cases. You receive a 15% discount.

Silver Member
We will reserve 1 case of our limited vintage to be delivered to you 6 bottles in May and 6 in Oct.
Single varietal or mixed cases. You receive a 10% discount.

To you exclusively from us not, available from any other retailers.

You will be invited to Velvet Roll Only Events and Tastings.
You will get preferential access to new and limited releases.
Members will be entered in a bi annual draw to win a 2 night stay here at the Ortel Weavers Lodge on the Freycinet Coast Tasmania.

Should not have
• VIP stamps,gimacs, anything that cheapens our brand.

We do not like busy posters please have white space

```html
<!DOCTYPE html>
<html lang="en">
<head>
<meta charset="utf-8">
<title>The Velvet Roll — Ortel Ridge Wine Club</title>
<link href="https://fonts.googleapis.com/css2?family=UnifrakturMaguntia&family=Delius&display=swap" rel="stylesheet">
<style>
  :root {
    --ink-light: #ffffff;
    --ink-soft: #d9d9d9;
    --night: #0b0b0b;
    --charcoal: #1c1c1c;
    --graphite: #3a3a3a;
    --silver-glow: #6e6e6e;
    --logo-ink: #111111;
    --logo-paper: #ffffff;
  }
  html, body {
    margin: 0;
    padding: 0;
    overflow: hidden;
    background: var(--night);
  }
  .poster {
    position: relative;
    width: 848px;
    height: 1200px;
    overflow: hidden;
    color: var(--ink-light);
    font-family: "Delius", "Trebuchet MS", sans-serif;
  }
  .still-life {
    position: absolute;
    inset: 0;
    background:
      radial-gradient(ellipse 40% 32% at 40% 36%, rgba(110,110,110,0.55), transparent 70%),
      radial-gradient(ellipse 26% 44% at 78% 56%, rgba(58,58,58,0.7), transparent 70%),
      radial-gradient(ellipse 38% 20% at 28% 86%, rgba(80,80,80,0.45), transparent 70%),
      linear-gradient(160deg, var(--graphite) 0%, var(--charcoal) 42%, var(--silver-glow) 62%, var(--night) 100%);
  }
  .headline {
    position: absolute;
    left: 50px;
    top: 150px;
    margin: 0;
    font-family: "UnifrakturMaguntia", "Old English Text MT", serif;
    font-weight: 400;
    font-size: 62px;
    line-height: 88px;
    letter-spacing: 1px;
    text-shadow: 0 2px 4px rgba(0,0,0,0.6);
  }
  .membership-limit {
    position: absolute;
    left: 43px;
    top: 520px;
    margin: 0;
    font-size: 18.5px;
    line-height: 28.5px;
    color: var(--ink-soft);
    text-shadow: 0 1px 2px rgba(0,0,0,0.6);
  }
  .membership-tiers {
    position: absolute;
    left: 43px;
    top: 568px;
    margin: 0;
    font-size: 18.5px;
    line-height: 28.5px;
    text-shadow: 0 1px 2px rgba(0,0,0,0.6);
  }
  .brand-mark {
    position: absolute;
    left: 475px;
    top: 824px;
    width: 195px;
    height: 102px;
    background: var(--logo-paper);
    display: flex;
    align-items: center;
    justify-content: center;
    font-family: "Delius", "Trebuchet MS", sans-serif;
    font-size: 30px;
    color: var(--logo-ink);
  }
  .exclusivity {
    position: absolute;
    left: 450px;
    top: 950px;
    margin: 0;
    text-shadow: 0 1px 2px rgba(0,0,0,0.6);
  }
  .exclusivity-note {
    display: block;
    font-size: 20px;
    line-height: 30px;
  }
  .exclusivity-claim {
    display: block;
    font-size: 25px;
    line-height: 36px;
  }
  .privileges {
    position: absolute;
    left: 28px;
    top: 1090px;
    margin: 0;
    text-shadow: 0 1px 2px rgba(0,0,0,0.6);
  }
  .privilege-main {
    display: block;
    font-size: 27px;
    line-height: 38px;
  }
  .privilege-sub {
    display: block;
    font-size: 15px;
    line-height: 26px;
    padding-left: 3px;
  }
</style>
</head>
<body>
  <main class="poster">
    <div class="still-life" role="img" aria-label="Monochrome still life of a wine bottle, a glass of white wine, a hanging bunch of grapes with vine leaves and scattered hazelnuts on an aged wall background"></div>

    <h1 class="headline">You are invited<br>to Join<br>The Velvet Roll!</h1>

    <p class="membership-limit">Only 1600 cases each vintage. Membership limited to 001–999.</p>

    <p class="membership-tiers">
      We commit two type of memberships:<br>
      Gold Membership: Reserve 2 cases of Wine delivered to you<br>
      1 May 1 Oct You choose the variety 15% DISCOUNT<br>
      Silver Membership: Reserve 1 case of your choice of wine delivered to you<br>
      6 bottles 1 May, 6 bottles 1 Oct you choose your variety 10% DISCOUNT
    </p>

    <div class="brand-mark">Ortel Ridge</div>

    <p class="exclusivity">
      <span class="exclusivity-note">Not available with other retailers</span>
      <span class="exclusivity-claim">Exclusively to you from us.</span>
    </p>

    <p class="privileges">
      <span class="privilege-main">VIP access to Velvet Roll only&nbsp; tastings and events</span>
      <span class="privilege-sub">Preferential access to first releases and limited releases</span>
      <span class="privilege-sub">Bi-annual draw to win a 2 night stay at the Ortel Weavers Lodge, Freycinet Coast</span>
    </p>
  </main>
</body>
</html>
```